TITLE: What Lifts a Young Player Past the Bench? SUB-TITLE: A Family’s Plain Talk Manual for Coaching...

My book is for parents who have young children that are really into sports. My book empowers parents so they can motivate their children to succeed. It deals with sports psychology. Both my title and subtitle should be easy to read. Ideally, I would like a picture of young athlete(s) on the title. I have uploaded files of some books on Brindlemart that deal with the same subject. The last two files are 1) my company logo, please try to include these colors 2) an ebook cover I put together myself. You will notice an On-line bonus in the middle of the book, this Bonus needs to be on the cover.

Target Market(s)

Parents with children who play sports at a high level

Colors

Designer to choose colors to be used in the design.

Requirements
Must have
• Online Bonus feature as per my example.
• Dimensions: Paperlyn = The ideal size of your eBook cover art is a height/width ratio of 1.6:1. This means that for every 1,000 pixels in width, the image should be 1,600 pixels in height.
Nice to have
• picture of a young athlete or young athletes

```html
<!DOCTYPE html>
<html lang="en">
<head>
<meta charset="utf-8">
<title>What Lifts a Young Player Past the Bench? — Book Cover</title>
<link href="https://fonts.googleapis.com/css2?family=Alfa+Slab+One&family=Questrial&display=swap" rel="stylesheet">
<style>
  :root {
    --page-bg: #e4e4e4;
    --cover-deep: #2a1238;
    --cover-plum: #45204f;
    --cover-wine: #5a2438;
    --cover-violet: #4a2a78;
    --band-mauve: #6b2c4a;
    --title-white: #ffffff;
    --title-orange: #f7931e;
    --title-edge: #1e0c28;
    --author-orange: #f0902a;
    --badge-ink: #2a1238;
  }
  * { margin: 0; padding: 0; box-sizing: border-box; }
  html, body {
    width: 1200px;
    height: 999px;
    overflow: hidden;
    background: var(--page-bg);
  }
  .canvas {
    position: relative;
    width: 1200px;
    height: 999px;
  }
  .book-cover {
    position: absolute;
    left: 401px;
    top: 194px;
    width: 418px;
    height: 627px;
    overflow: hidden;
    background:
      radial-gradient(ellipse at 15% 20%, var(--cover-wine) 0%, transparent 55%),
      radial-gradient(ellipse at 70% 70%, var(--cover-violet) 0%, transparent 60%),
      linear-gradient(180deg, var(--cover-deep) 0%, var(--cover-plum) 100%);
  }
  .cover-photo {
    position: absolute;
    left: 111px;
    top: 232px;
    width: 192px;
    height: 250px;
    background:
      radial-gradient(ellipse at 75% 40%, rgba(247,147,30,0.6) 0%, rgba(60,110,230,0.35) 24%, transparent 48%),
      radial-gradient(ellipse at 25% 78%, rgba(247,147,30,0.45) 0%, transparent 32%),
      linear-gradient(180deg, rgba(20,10,30,0.5) 0%, rgba(40,20,60,0.15) 100%);
    border-radius: 30px;
  }
  .cover-title {
    position: absolute;
    left: 0;
    right: 0;
    top: 20px;
    text-align: center;
    font-family: "Alfa Slab One", serif;
    font-weight: 400;
    line-height: 1;
  }
  .cover-title span {
    display: block;
    text-shadow:
      2px 0 0 var(--title-edge), -2px 0 0 var(--title-edge),
      0 2px 0 var(--title-edge), 0 -2px 0 var(--title-edge),
      2px 2px 0 var(--title-edge), -2px -2px 0 var(--title-edge),
      2px -2px 0 var(--title-edge), -2px 2px 0 var(--title-edge);
  }
  .title-small {
    color: var(--title-white);
    font-size: 25px;
    letter-spacing: 1px;
    margin: 5px 0 3px;
  }
  .title-large {
    color: var(--title-orange);
    font-size: 50px;
    letter-spacing: 2px;
  }
  .title-final {
    color: var(--title-white);
    font-size: 38px;
    letter-spacing: 2px;
    margin-top: 4px;
  }
  .bonus-badge {
    position: absolute;
    left: 26px;
    top: 262px;
    width: 74px;
    height: 74px;
    border-radius: 50%;
    background: var(--title-orange);
    display: flex;
    align-items: center;
    justify-content: center;
    text-align: center;
    font-family: "Questrial", sans-serif;
    font-size: 12px;
    line-height: 1.2;
    color: var(--badge-ink);
    text-transform: uppercase;
  }
  .cover-subtitle {
    position: absolute;
    left: 50px;
    right: 50px;
    top: 498px;
    text-align: center;
    font-family: "Questrial", sans-serif;
    color: var(--title-white);
    font-size: 16px;
    line-height: 1.3;
    text-transform: uppercase;
  }
  .author-band {
    position: absolute;
    left: 0;
    right: 0;
    bottom: 0;
    height: 60px;
    background: linear-gradient(180deg, rgba(107,44,74,0) 0%, var(--band-mauve) 40%);
  }
  .cover-author {
    position: absolute;
    left: 0;
    right: 0;
    bottom: 10px;
    text-align: center;
    font-family: "Questrial", sans-serif;
    color: var(--author-orange);
    font-size: 34px;
    letter-spacing: 0.5px;
  }
  .spine-edge {
    position: absolute;
    left: 0;
    top: 0;
    width: 7px;
    height: 100%;
    background: linear-gradient(90deg, rgba(255,255,255,0.12), rgba(0,0,0,0.25));
  }
</style>
</head>
<body>
<div class="canvas">
  <div class="book-cover">
    <div class="cover-photo" role="img" aria-label="Photo of a young runner's legs mid-stride, shoe soles lit in orange and blue against purple haze"></div>
    <h1 class="cover-title">
      <span class="title-small">WHAT LIFTS A</span>
      <span class="title-large">YOUNG</span>
      <span class="title-small">PLAYER PAST</span>
      <span class="title-large">THE</span>
      <span class="title-final">BENCH?</span>
    </h1>
    <div class="bonus-badge">Online<br>Bonus<br>Inside</div>
    <p class="cover-subtitle">A Family’s Plain Talk Manual for Coaching Confident, Focused and Resilient Athletes</p>
    <div class="author-band"></div>
    <p class="cover-author">REN VALDOSTA</p>
    <div class="spine-edge"></div>
  </div>
</div>
</body>
</html>
```